Iconic Cool Labels for Amazing Coffee

I'm back again after a very successful logo design project, now looking for label designs!

NOTEs:

IF YOU SUBMIT A DESIGN YOU WILL DEFINITELY RECEIVE FEEDBACK. I think it's rude not to respond when somebody takes the time to devote their time and talent to a project like this.

THIS BRIEF IS LONG. Out of respect for you, the designers. I've put a lot of time into this to give you as much understanding as I can. I think if you are going to invest your time it is only right and proper that I do the same. So please don't be put off by the length - it is intended to save you time and energy.

THE BRIEF

We are launching a coffee website called Brewvantia aimed at those who really care about coffee and have a passion for getting the very best out of it. So far, we have a great logo (attached), we have the website under construction and with the look and feel decided.

We are not a mass market player - instead we are more like an online boutique. But, we are starting out and need to look chic in a way that doesn't involve large investments. So, our coffee will be packaged in bags (1kg and 250g) with brown paper exteriors (brown kraft) onto which we'll put self adhesive labels.This is where we need your help.

THE TASK
- Create the 2 "master" labels for the front of the bags
- Create the variety labels that go either on or somewhere around the master label
- Create a small label for the back of the bag that contains the required regulatory information

There are 2 "families" - each requiring a family label. They are our blends (there are 7 of these), our single origin coffees (there are 3 of these) and the fair trade organic.

MASTER LABELS - In my mind the main focus of this brief
For the front of the bag there will be a master label for each of the 2 families, with another self-adhesive label placed either on top of the master label or adjacent to it. The exception being the free trade organic - there is only one of these, so no over labelling required.

The master labels are the main game here. They need to be distinctive and tasteful. They should look "chic" but not "try hard". They should be different to each other yet clearly part of the same house.

Both master labels MUST include the Brewvantia logo (supplied) and must also include a small Tornaso logo somewhere. Tornaso is our roaster. Perhaps it might be "Proudly roasted by (Tornaso logo)", or something like that.

The master labels are needed in each of the 1kg and 250g sizes and should have the size displayed as a part of the label.

The 2 master labels are:
Blends - these are beans from multiple origins and are typically used for espresso, late etc. I'd prefer that the label doesn't say "blends".

Single Origin - these are coffees from a single place in the world. They are for enthusiasts who want to explore the nuance and subtlety of a single region. Rather than be made in an espresso machine (although they can be) siphons are where these truly come in to their own.

VARIETY LABEL
These will either be stuck in a designated space on the MASTER LABEL or will be stuck somewhere else on the usable area. There are 7 of these in the blends family and 3 in the single origins family. They may be all very similar in look and feel or they may be variations within a theme. What do you think they should be?

You may decide to make them look similar of different. You might have groups - e.g. the first four, the free trade organics and the decafs. (Though if you do please don't do the cliched thing and make the decafs blue!)

Our Varieties are:
BLENDS
The Waypost
The Devotee
The Sybarite
The Revelist
Free Trade Organic
Swiss Decafeinated
Mexican Mountain Decafeinated

SINGLE ORIGIN
Ethiopian Limou
Costa Rica La Lapa
Nicaraguan Marigogipe Superior

COMPLIANCE LABEL
This is a small label to go onto the back of the bag for all of our coffees. It contains all of the regulatory and compliance information. I'd like this to be small and reasonably unobtrusive, but clearly from the same "stable" as the other labels. This should be a regular shape so it's easy and quick to stick on, but not necessarily a rectangle - you pick.

It should contain:

Brewvantia
PO Box 4736
Ellmore VIC 3190
www.brewvantia.com.au

Roasted, Blended & Packed in Australia
from Imported Beans

Store away from sunlight in a cool dry place

TECHNICAL DETAILS
The usable areas are (in portrait format)
1kg - 180mm high by 100mm wide
250g - 140mm high by 70mm wide

How much of this space you use and how you use it is up to you. My ingoing feeling is that using all of the available space would make it look "mass market" rather than premium. On the front, maybe there are a couple of small labels that are spaced, maybe there's one big label with an over sticker. I don't want to constrain you too much in this regard - except to say that unusual shapes like stars may be both slow and awkward to put onto the bags

THE CREATIVE SIDE
This is where you come in...
- Do you use all the space of just some of it (my guess is the latter)?
- One master on the front with an oversticker for variety or 2 separate labels?
- Rectangular labels or another shape (not jagged shapes please - too hard to stick evenly)
- Does the label contain, just words or does it have images, photos etc?
- Are the variety labels all similar or do they have a different look and feel?

ATTACHMENTS
- Brewvantia logo pack in zip file
- Tornaso logo
- Some photos I shared for the logo brief as examples
Updates

All, 

The files I thought I'd attached didn't get there the first time. I think I've corrected that now. Sorry for any hassle caused.

Cheers,
Gus

Target Market(s)

Our target customers have one thing in common - they are passionate about excellent coffee. While they come from all walks of life the image in my head is of young professionals that wear designer clothes - lots of black - and are passionate about design. They aspire to have Lurst furniture and care passionately about both design and functionality. They go to the cinema, but mainly arthouse and foreign. They visit the theatre and art galleries. They care about their coffee and the making of it might even be described as a ritual. They have separate grinders and espresso machines and are especially particular about everything to do with coffee - the beans (where they come from and how they are roasted), the grind, the making of the coffee itself, right down to the cups and glasses in which they are served.

Industry/Entity Type

Construction

Requirements
Must have
• A look and feel of premiumness without being staid. I think companies that have done this incredible well include Veltro, Sorna, Quell, Darui, KTR. They are clearly premium, but have a feeling of what I describe as understated cutting edge about them. There is a lot of work that has gone into all of their graphic material yet they don't look "try hard".The colour palate is quite narrow - black, white, silver/chrome, and various coffee shades ranging perhaps from the golden brown of the crema to the rich dark brown of a roasted bean.
Nice to have
• I would like the coffee bag to be something that people leave out because it looks cool an chic.
Should not have
• Please avoid the cliches. I was thrilled with the creativity in the logo work, so I am enthusiastic at the prospect of seeing the same here.

Importantly, please avoid steaming cups at all costs! Also, pictures of people sipping coffee and looking blissfully content are not what I'm looking for.

Also, out emphasis is italian style coffee - espresso, late etc rather than the long black coffee that comes out of a filter machine that is popular in the US - consequently images that connote that should be avoided.

```html
<!DOCTYPE html>
<html lang="en">
<head>
<meta charset="utf-8">
<title>Brewvantia – Bag Label Family</title>
<link rel="stylesheet" href="https://fonts.googleapis.com/css2?family=Jost:wght@400;500&family=PT+Sans:wght@400&family=Libre+Baskerville:wght@400&display=swap">
<style>
  :root {
    --kraft: #c49a62;
    --ink: #1a1410;
    --bean: #3a1f14;
    --label-white: #ffffff;
    --frame: #111111;
    --slot-line: #8a9aa0;
    --slot-text: #7a8c92;
    --url-red: #e0201a;
    --roaster-navy: #1e2a5a;
    --espresso-red: #d4533a;
    --crema-gold: #c9a664;
    --single-green: #2a8c66;
    --organic-olive: #6b7a2a;
    --maroon: #5a1510;
    --wordmark: "Jost", "Futura", sans-serif;
    --body: "PT Sans", "Helvetica Neue", sans-serif;
    --display: "Libre Baskerville", Georgia, serif;
  }
  html, body { margin: 0; padding: 0; overflow: hidden; }
  .canvas {
    position: relative;
    width: 1200px;
    height: 900px;
    background: var(--kraft);
    overflow: hidden;
  }
  .label { position: absolute; display: block; }
  .label--front-espresso { left: 38px;  top: 93px; }
  .label--front-single   { left: 427px; top: 92px; }
  .label--front-organic  { left: 830px; top: 92px; }
  .label--back-espresso  { left: 36px;  top: 604px; }
  .label--back-single    { left: 430px; top: 607px; }
  .label--back-organic   { left: 834px; top: 609px; }

  .family-name {
    position: absolute;
    margin: 0;
    font-family: var(--display);
    font-weight: 400;
    font-size: 38px;
    color: var(--ink);
    line-height: 1;
  }
  .family-name--blended { left: 116px; top: 474px; }
  .family-name--organic { left: 927px; top: 464px; }

  .wordmark { font-family: var(--wordmark); font-weight: 500; fill: var(--bean); letter-spacing: 5px; }
  .slot-frame { fill: none; stroke: var(--slot-line); stroke-width: 1.5; }
  .slot-text { font-family: var(--body); font-size: 11.5px; fill: var(--slot-text); }
  .size-mark { font-family: var(--body); font-size: 11px; fill: var(--ink); }
  .fine-print { font-family: var(--body); font-size: 7.5px; fill: var(--ink); }
  .roaster-name { font-family: var(--body); font-size: 8.5px; fill: var(--roaster-navy); }
  .tagline { font-family: var(--body); font-size: 5.6px; fill: var(--ink); }
  .address { font-family: var(--body); font-size: 12px; fill: var(--ink); }
  .web-address { font-family: var(--body); font-size: 8px; fill: var(--url-red); }
  .brand-dot { fill: var(--bean); stroke: var(--label-white); stroke-width: 2; }
  .roaster-dot { fill: var(--roaster-navy); }
  .silhouette { fill: var(--label-white); stroke: var(--frame); stroke-width: 2; }
  .back-panel { fill: var(--label-white); stroke: #333; stroke-width: 1; }
</style>
</head>
<body>
<main class="canvas">

  <!-- Front label: espresso family -->
  <svg class="label label--front-espresso" width="338" height="264" viewBox="0 0 338 264" aria-label="Brewvantia 1kg front label, espresso family">
    <defs>
      <linearGradient id="awning-espresso-tone" x1="0" x2="1" y1="0" y2="0">
        <stop offset="0" stop-color="var(--espresso-red)"/>
        <stop offset="0.5" stop-color="var(--crema-gold)"/>
        <stop offset="1" stop-color="var(--espresso-red)"/>
      </linearGradient>
    </defs>
    <path class="silhouette" d="M1,1 H337 V70 Q337,84 331,88 V263 H7 V88 Q1,84 1,70 Z"/>
    <rect x="8" y="9" width="322" height="76" fill="url(#awning-espresso-tone)" role="img" aria-label="Striped shop awning in red and crema gold"/>
    <circle class="brand-dot" cx="170" cy="38" r="17"/>
    <text class="wordmark" x="172" y="73" font-size="12" text-anchor="middle">BREWVANTIA</text>
    <rect class="slot-frame" x="76" y="120" width="184" height="56"/>
    <text class="slot-text" x="168" y="142" text-anchor="middle">Variety Label</text>
    <text class="slot-text" x="168" y="155" text-anchor="middle">goes here</text>
    <text class="size-mark" x="26" y="236">1kg</text>
    <text class="fine-print" x="280" y="236" text-anchor="end">Roasted to perfection by</text>
    <circle class="roaster-dot" cx="287" cy="233" r="3"/>
    <text class="roaster-name" x="322" y="236" text-anchor="end" textLength="30" lengthAdjust="spacingAndGlyphs">Tornaso</text>
  </svg>

  <!-- Front label: single origin family -->
  <svg class="label label--front-single" width="338" height="264" viewBox="0 0 338 264" aria-label="Brewvantia 1kg front label, single origin family">
    <path class="silhouette" d="M1,1 H337 V70 Q337,84 331,88 V263 H7 V88 Q1,84 1,70 Z"/>
    <rect x="8" y="9" width="322" height="76" fill="var(--single-green)" role="img" aria-label="Striped shop awning in green and white"/>
    <circle class="brand-dot" cx="170" cy="38" r="17"/>
    <text class="wordmark" x="172" y="73" font-size="12" text-anchor="middle">BREWVANTIA</text>
    <rect class="slot-frame" x="76" y="120" width="184" height="56"/>
    <text class="slot-text" x="168" y="142" text-anchor="middle">Variety Label</text>
    <text class="slot-text" x="168" y="155" text-anchor="middle">goes here</text>
    <text class="size-mark" x="26" y="236">1kg</text>
    <text class="fine-print" x="280" y="236" text-anchor="end">Roasted to perfection by</text>
    <circle class="roaster-dot" cx="287" cy="233" r="3"/>
    <text class="roaster-name" x="322" y="236" text-anchor="end" textLength="30" lengthAdjust="spacingAndGlyphs">Tornaso</text>
  </svg>

  <!-- Front label: organic -->
  <svg class="label label--front-organic" width="338" height="264" viewBox="0 0 338 264" aria-label="Brewvantia 1kg front label, organic">
    <path class="silhouette" d="M1,1 H337 V70 Q337,84 331,88 V263 H7 V88 Q1,84 1,70 Z"/>
    <rect x="8" y="9" width="322" height="76" fill="var(--organic-olive)" role="img" aria-label="Striped shop awning in olive and white"/>
    <circle class="brand-dot" cx="168" cy="38" r="17"/>
    <text class="wordmark" x="170" y="73" font-size="12" text-anchor="middle">BREWVANTIA</text>
    <rect class="slot-frame" x="74" y="120" width="184" height="56"/>
    <text class="slot-text" x="166" y="142" text-anchor="middle">Variety Label</text>
    <text class="slot-text" x="166" y="155" text-anchor="middle">goes here</text>
    <text class="size-mark" x="24" y="236">1kg</text>
    <text class="fine-print" x="280" y="236" text-anchor="end">Roasted to perfection by</text>
    <circle class="roaster-dot" cx="287" cy="233" r="3"/>
    <text class="roaster-name" x="322" y="236" text-anchor="end" textLength="30" lengthAdjust="spacingAndGlyphs">Tornaso</text>
  </svg>

  <h2 class="family-name family-name--blended">Blended</h2>
  <h2 class="family-name family-name--organic">Organic</h2>

  <!-- Back compliance labels -->
  <svg class="label label--back-espresso" width="338" height="264" viewBox="0 0 338 264" aria-label="Brewvantia compliance label, espresso family">
    <path d="M0,0 H338 V60 Q338,78 332,82 V264 H6 V82 Q0,78 0,60 Z" fill="var(--maroon)" stroke="#2a0a06" stroke-width="1"/>
    <rect class="back-panel" x="14" y="22" width="310" height="222"/>
    <circle class="brand-dot" cx="168" cy="42" r="18"/>
    <text class="wordmark" x="170" y="78" font-size="13" text-anchor="middle">BREWVANTIA</text>
    <text class="tagline" x="168" y="88" text-anchor="middle">Roasted, Blended &amp; Packed in Australia from Imported Beans</text>
    <text class="address" x="168" y="131" text-anchor="middle">Brewvantia</text>
    <text class="address" x="168" y="146" text-anchor="middle">PO Box 4736</text>
    <text class="address" x="168" y="161" text-anchor="middle">Ellmore VIC 3190</text>
    <text class="web-address" x="168" y="171" text-anchor="middle">www.brewvantia.com.au</text>
    <text class="fine-print" x="19" y="238">Store away from sunlight in a cool dry place</text>
    <text class="fine-print" x="276" y="238" text-anchor="end">Roasted to perfection by</text>
    <circle class="roaster-dot" cx="283" cy="235" r="3"/>
    <text class="roaster-name" x="318" y="238" text-anchor="end" textLength="30" lengthAdjust="spacingAndGlyphs">Tornaso</text>
  </svg>

  <svg class="label label--back-single" width="338" height="264" viewBox="0 0 338 264" aria-label="Brewvantia compliance label, single origin family">
    <path d="M0,0 H338 V60 Q338,78 332,82 V264 H6 V82 Q0,78 0,60 Z" fill="var(--single-green)" stroke="#174a36" stroke-width="1"/>
    <rect class="back-panel" x="14" y="22" width="310" height="222"/>
    <circle class="brand-dot" cx="168" cy="42" r="18"/>
    <text class="wordmark" x="170" y="78" font-size="13" text-anchor="middle">BREWVANTIA</text>
    <text class="tagline" x="168" y="88" text-anchor="middle">Roasted, Blended &amp; Packed in Australia from Imported Beans</text>
    <text class="address" x="168" y="131" text-anchor="middle">Brewvantia</text>
    <text class="address" x="168" y="146" text-anchor="middle">PO Box 4736</text>
    <text class="address" x="168" y="161" text-anchor="middle">Ellmore VIC 3190</text>
    <text class="web-address" x="168" y="171" text-anchor="middle">www.brewvantia.com.au</text>
    <text class="fine-print" x="19" y="238">Store away from sunlight in a cool dry place</text>
    <text class="fine-print" x="276" y="238" text-anchor="end">Roasted to perfection by</text>
    <circle class="roaster-dot" cx="283" cy="235" r="3"/>
    <text class="roaster-name" x="318" y="238" text-anchor="end" textLength="30" lengthAdjust="spacingAndGlyphs">Tornaso</text>
  </svg>

  <svg class="label label--back-organic" width="338" height="264" viewBox="0 0 338 264" aria-label="Brewvantia compliance label, organic">
    <path d="M0,0 H338 V60 Q338,78 332,82 V264 H6 V82 Q0,78 0,60 Z" fill="var(--organic-olive)" stroke="#3c4416" stroke-width="1"/>
    <rect class="back-panel" x="14" y="22" width="310" height="222"/>
    <circle class="brand-dot" cx="168" cy="42" r="18"/>
    <text class="wordmark" x="170" y="78" font-size="13" text-anchor="middle">BREWVANTIA</text>
    <text class="tagline" x="168" y="88" text-anchor="middle">Roasted, Blended &amp; Packed in Australia from Imported Beans</text>
    <text class="address" x="168" y="131" text-anchor="middle">Brewvantia</text>
    <text class="address" x="168" y="146" text-anchor="middle">PO Box 4736</text>
    <text class="address" x="168" y="161" text-anchor="middle">Ellmore VIC 3190</text>
    <text class="web-address" x="168" y="171" text-anchor="middle">www.brewvantia.com.au</text>
    <text class="fine-print" x="19" y="238">Store away from sunlight in a cool dry place</text>
    <text class="fine-print" x="276" y="238" text-anchor="end">Roasted to perfection by</text>
    <circle class="roaster-dot" cx="283" cy="235" r="3"/>
    <text class="roaster-name" x="318" y="238" text-anchor="end" textLength="30" lengthAdjust="spacingAndGlyphs">Tornaso</text>
  </svg>

</main>
</body>
</html>
```